Flyer/Poster to promote Bicycle Race

We need a flyer that promotes a bicycle race in downtown Denver. It need to inspire spectators to come watch and bicycle racers to come race. It benefits the Tall Pines Cycling Club is getting urban kids on bikes; sharing healthy lifestyle and values
. We want the colors to be the colors of the logo - blue & red. Community Partnerships must have their logos on the flyer. Flyer must be able to be printed in 8 1/2 x 11 and 11 x 17

Target Market(s)

Neighborhood residents, athletes, cyclists

Industry/Entity Type

Non Profit

Font styles to use
Serif
Sans Serif

Colors
0592cd
ec1f27

Requirements
Must have
• Sunday, July 31, 2016
• Schedule:
• • Racing starts at 7:00am
• • Fun Ride on the Race Course at 12pm
• • Expo & Festival 10am – 6pm
• A Bike Race for Amateurs and Professionals
• A Bike Race for the young, the old & everyone in the middle.
• Great for spectators. Hang out, watch the action & explore the Festival
• Grab a bite to eat & cheer on the racers as they fly around the corners
• Special activities for kids: Wobblo Course, Maple the Moose & More!!
• Renaldo Vasquez KPLT Music Director and Crosstown Groove Hour host will be onsite!
• Start/Finish/Festival will be on Larkwell St between 9th Ave & 11th Ave
• Net proceeds benefit the Tall Pines Cycling Club dedicated to getting urban youth on bikes; sharing healthy lifestyle and values
• Special thanks to the Harrowgate Foundation for their ongoing support
• LARKWELLSTCRIT.COM

```html
<!DOCTYPE html>
<html lang="en">
<head>
<meta charset="utf-8">
<title>Larkwell St Crit – Bicycle Race Poster</title>
<link rel="stylesheet" href="https://fonts.googleapis.com/css2?family=Roboto+Condensed:wght@400;700&display=swap">
<style>
  :root {
    --red: #ec1f27;
    --blue: #0592cd;
    --ink: #1e1e1e;
    --grey: #bdbdbd;
    --grey-light: #ececec;
    --paper: #ffffff;
    --stage: #d9d9d9;
  }
  html, body {
    margin: 0; padding: 0;
    width: 1200px; height: 960px;
    overflow: hidden;
    background: var(--stage);
    font-family: "Roboto Condensed", sans-serif;
    color: var(--ink);
  }
  .poster {
    position: absolute;
    left: 332px; top: 44px;
    width: 710px; height: 1095px;
    background: var(--paper);
    transform: scale(0.8);
    transform-origin: top left;
    overflow: hidden;
  }
  .abs { position: absolute; white-space: nowrap; }
  .art { position: absolute; left: 0; top: 0; width: 710px; height: 1095px; }

  .club-name {
    left: 28px; top: 78px;
    font-weight: 700; font-size: 30px; line-height: 1.05;
    color: var(--ink); letter-spacing: 0.5px;
    display: flex; align-items: flex-start; gap: 8px;
  }
  .club-name .mark { width: 14px; height: 14px; background: var(--red); flex: none; margin-top: 8px; }

  .organize {
    left: 342px; top: 205px;
    transform: rotate(-90deg); transform-origin: left top;
    font-size: 44px; font-weight: 700; line-height: 1; color: var(--ink);
  }
  .headline { left: 386px; font-weight: 700; line-height: 1; letter-spacing: -1px; font-size: 84px; }
  .headline.bicycle { top: 54px; color: var(--red); }
  .headline.race { top: 133px; color: var(--blue); }

  .date { left: 573px; top: 138px; width: 95px; height: 64px; color: var(--ink); line-height: 1; }
  .date .on { font-size: 14px; }
  .date .day { font-size: 25px; }
  .date .num { position: absolute; top: 30px; left: 0; font-size: 34px; }
  .date .num sup { font-size: 18px; vertical-align: 12px; }
  .date .month { position: absolute; top: 32px; left: 56px; font-size: 17px; font-weight: 700; line-height: 0.95; text-align: right; }

  .rule { left: 343px; top: 215px; width: 367px; height: 1px; background: #777; }

  .start-time { left: 343px; top: 220px; font-size: 35px; line-height: 1.1; }
  .venue-label { left: 343px; top: 262px; font-size: 13px; font-weight: 700; }
  .venue { left: 343px; top: 276px; font-size: 19px; letter-spacing: 0.4px; }
  .venue sup { font-size: 10px; }

  .highlights {
    left: 343px; top: 318px; width: 340px;
    margin: 0; padding: 0; list-style: none; white-space: normal;
    font-size: 13.5px; line-height: 16.5px; letter-spacing: 0.3px; color: var(--ink);
  }
  .highlights li { position: relative; padding-left: 13px; margin-bottom: 6.8px; }
  .highlights li::before {
    content: ""; position: absolute; left: 0; top: 3px;
    border-left: 8px solid var(--red);
    border-top: 5px solid transparent; border-bottom: 5px solid transparent;
  }

  .kids-title { left: 18px; top: 916px; font-size: 21px; }
  .kids-list { left: 18px; top: 945px; font-size: 15.5px; line-height: 21px; }

  .site { left: 376px; top: 961px; font-size: 32px; font-weight: 700; letter-spacing: 0.8px; }

  .thanks { left: 16px; top: 1008px; font-size: 16px; font-weight: 700; letter-spacing: 0.3px; }

  .partners {
    left: 14px; top: 1040px; width: 680px; height: 44px;
    display: flex; align-items: center; justify-content: space-between;
  }
  .partner { font-size: 11px; font-weight: 700; color: var(--ink); text-align: center; white-space: nowrap; }
  .partner.red { color: var(--red); }
  .partner.blue { color: var(--blue); }
  .partner-badge { width: 32px; height: 32px; background: #8a8a8a; border-radius: 50%; }
  .partner-badge.square { border-radius: 2px; background: var(--ink); }
  .partner-badge.redbadge { background: var(--red); }
</style>
</head>
<body>
<main class="poster">
  <svg class="art" viewBox="0 0 710 1095">
    <defs>
      <linearGradient id="racePhoto" x1="0" y1="0" x2="1" y2="1">
        <stop offset="0" stop-color="#6b6f63"/>
        <stop offset="0.45" stop-color="#8a4a8f"/>
        <stop offset="1" stop-color="#5f6068"/>
      </linearGradient>
      <linearGradient id="kidsPhoto" x1="0" y1="0" x2="1" y2="1">
        <stop offset="0" stop-color="#e63946"/>
        <stop offset="1" stop-color="#f29ac0"/>
      </linearGradient>
      <linearGradient id="texture" x1="0" y1="0" x2="0" y2="1">
        <stop offset="0" stop-color="#f2f2f2"/>
        <stop offset="1" stop-color="#ffffff"/>
      </linearGradient>
    </defs>
    <rect x="440" y="40" width="270" height="520" fill="url(#texture)"
          role="img" aria-label="Faint background texture of racing cyclists"/>
    <path d="M0 690 L0 1000 L150 1000 L300 700 L320 300 L310 150 L240 175 L110 420 Z"
          fill="var(--grey)" role="img" aria-label="Large grey illustration of a clock tower"/>
    <polygon points="170,550 355,648 115,720" fill="var(--red)"/>
    <polygon points="170,550 176,537 362,646 355,648" fill="var(--blue)"/>
    <polygon points="125,734 710,552 710,955 320,955 240,905 255,878"
             fill="url(#racePhoto)" role="img" aria-label="Photo of women cyclists racing through a downtown corner"/>
    <ellipse cx="95" cy="835" rx="76" ry="82" fill="url(#kidsPhoto)"
             role="img" aria-label="Photo of a child hugging the festival mascot"/>
  </svg>

  <div class="abs club-name"><span class="mark"></span><span>THE<br>LARKWELL ST<br>CRIT</span></div>

  <div class="abs organize">organize</div>
  <div class="abs headline bicycle">BICYCLE</div>
  <div class="abs headline race">RACE</div>

  <div class="abs date">
    <span class="on">On</span> <span class="day">Sunday</span>
    <div class="num">31<sup>th</sup></div>
    <div class="month">July<br>2016</div>
  </div>

  <div class="abs rule"></div>
  <div class="abs start-time">Racing starts at 7:00am</div>
  <div class="abs venue-label">Start/Finish/Festival will be on</div>
  <div class="abs venue">Larkwell St between 9<sup>th</sup> Ave &amp; 11<sup>th</sup> Ave</div>

  <ul class="abs highlights">
    <li>Fun Ride on the Race Course at 12pm</li>
    <li>Expo &amp; Festival 10am – 6pm</li>
    <li>A Bike Race for Amateurs and Professionals</li>
    <li>A Bike Race for the young, the old &amp; everyone in the middle.</li>
    <li>Great for spectators. Hang out, watch the action &amp;<br>explore the Festival</li>
    <li>Grab a bite to eat &amp; cheer on the racers as they fly around<br>the corners</li>
    <li>Renaldo Vasquez KPLT Music Director and Crosstown<br>Groove Hour host will be onsite!</li>
    <li>Net proceeds benefit the Tall Pines Cycling Club<br>dedicated to getting urban youth on bikes,<br>sharing healthy lifestyle and values</li>
  </ul>

  <div class="abs kids-title">Special activities for kids:</div>
  <div class="abs kids-list">Wobblo Course<br>Maple the Moose &amp; More!!</div>

  <div class="abs site">LARKWELLSTCRIT.COM</div>

  <div class="abs thanks">Special thanks to the Harrowgate Foundation for their ongoing support</div>

  <div class="abs partners">
    <span class="partner red">Corvane</span>
    <span class="partner">Silver Wedge</span>
    <span class="partner-badge"></span>
    <span class="partner">Pellavo</span>
    <span class="partner red">Tall Pines</span>
    <span class="partner-badge square"></span>
    <span class="partner">Brisa Racing</span>
    <span class="partner">KPLT</span>
    <span class="partner blue">Teamline</span>
    <span class="partner">Summit Public TV</span>
    <span class="partner-badge redbadge"></span>
  </div>
</main>
</body>
</html>
```